Restaurant Needs In House Signage Designed

We need a design to promote banquets/private events and happy hour. The design should be able to fit a small table tent as well as a large (roughly 4 feet tall) sign for our banquet space. The main focus should be private events with a small message about happy hour towards to bottom. Details about our event space, pictures and happy hour menus can be found on our website... www.pelbarkitchen.com

Target Market(s)

ages 25 to 50
middle to upper income

Industry/Entity Type

Restaurant

Font styles to use
Serif
Sans Serif

Colors

Designer to choose colors to be used in the design.

Requirements
Must have
• Pictures and attractive/eye-catching text/info
Nice to have
• logo

```html
<!DOCTYPE html>
<html lang="en">
<head>
<meta charset="utf-8">
<title>Pelbar Kitchen – Private Events Sign</title>
<link href="https://fonts.googleapis.com/css2?family=Great+Vibes&family=Raleway:ital,wght@0,400;0,500;0,600;1,400;1,500&display=swap" rel="stylesheet">
<style>
  :root {
    --backdrop: #e9e9e9;
    --paper: #ffffff;
    --ink: #2b2b2b;
    --orange: #ee7535;
    --lime: #b5cf3c;
    --social: #3b7ac4;
    --photo-warm: #6b4630;
    --photo-dark: #3a2b22;
    --photo-cool: #3c4a5c;
  }
  * { margin: 0; padding: 0; box-sizing: border-box; }
  html, body { width: 1200px; height: 1000px; overflow: hidden; }
  body { background: var(--backdrop); font-family: "Raleway", sans-serif; color: var(--ink); }

  .sign {
    position: absolute; left: 330px; top: 47px;
    width: 540px; height: 906px;
    background: var(--paper);
    box-shadow: 0 2px 10px rgba(0,0,0,.12);
    overflow: hidden;
  }
  .sign__title {
    position: absolute; top: 26px; left: 0; width: 100%;
    text-align: center;
    font-family: "Great Vibes", cursive;
    font-size: 34px; line-height: 38px; color: var(--ink);
  }
  .hero-photo {
    position: absolute; top: 150px; left: 0; width: 540px; height: 212px;
    background: radial-gradient(ellipse at 55% 45%, #d8b27a 0%, #8a5a38 45%, #3a2418 100%);
  }
  .swoosh { position: absolute; top: 105px; left: 0; width: 540px; height: 140px; }

  .photo-row { position: absolute; left: 0; width: 540px; height: 106px; display: flex; gap: 6px; }
  .photo-row--venue { top: 368px; }
  .photo-row--menu { top: 700px; }
  .photo { flex: 1; }
  .photo--dining { background: linear-gradient(135deg, #5a3a2a, #c9b9a8 60%, #3b2a20); }
  .photo--dessert { background: radial-gradient(circle at 50% 55%, #4a2a1a 0%, #8b6a55 40%, #e9e4df 75%); }
  .photo--bar { background: linear-gradient(160deg, #1e2c44, #4a6a8a 50%, #8a6a44); }
  .photo--pizza { background: radial-gradient(circle at 45% 60%, #c0462a 0%, #7a2a14 45%, #f09a3a 80%, #3a1a0a); }
  .photo--oysters { background: radial-gradient(circle at 50% 50%, #d7dcdf 0%, #8c8f90 50%, #3d3128 100%); }
  .photo--cocktails { background: linear-gradient(120deg, #b8c87a, #d96a4a 50%, #2a1e18); }

  .events { position: absolute; top: 490px; left: 0; width: 100%; text-align: center; }
  .events__heading { color: var(--orange); font-size: 23px; font-weight: 400; }
  .events__copy {
    margin: 8px auto 0; width: 440px;
    font-size: 12.5px; line-height: 17px; font-style: italic; font-weight: 500;
  }
  .divider { position: absolute; top: 588px; left: 30px; width: 480px; height: 6px; }

  .happy-hour { position: absolute; top: 603px; left: 0; width: 100%; text-align: center; }
  .happy-hour__heading { color: var(--orange); font-size: 21px; line-height: 25px; font-weight: 400; }
  .happy-hour__menu { margin-top: 5px; font-size: 13px; line-height: 16px; font-weight: 500; }

  .reserve-bar {
    position: absolute; top: 812px; left: 0; width: 540px; height: 28px;
    background: var(--lime); text-align: center;
    font-size: 16px; line-height: 28px; font-weight: 500; letter-spacing: .4px;
  }
  .brand {
    position: absolute; top: 854px; left: 18px;
    font-size: 15px; font-weight: 600; line-height: 18px; color: var(--ink);
    width: 70px;
  }
  .website { position: absolute; top: 866px; left: 0; width: 100%; text-align: center; font-size: 13px; }
  .social { position: absolute; top: 862px; right: 22px; display: flex; gap: 4px; }
  .social__square { width: 18px; height: 18px; border-radius: 3px; background: var(--social); }
</style>
</head>
<body>
  <main class="sign">
    <h1 class="sign__title">Walnut Creek's<br>Premiere Dining Destinations</h1>

    <div class="hero-photo" role="img" aria-label="Guests raising champagne glasses in a toast"></div>
    <svg class="swoosh" viewBox="0 0 540 140" preserveAspectRatio="none" aria-hidden="true">
      <path d="M0,0 H540 V58 C350,16 150,36 0,80 Z" fill="#ffffff"/>
      <path d="M0,80 C150,36 350,16 540,58 L540,86 C380,62 200,78 0,118 Z" fill="#ee7535"/>
      <path d="M0,118 C200,78 380,62 540,86 L540,112 C380,92 200,104 0,140 Z" fill="#b5cf3c"/>
    </svg>

    <div class="photo-row photo-row--venue">
      <div class="photo photo--dining" role="img" aria-label="Private dining room set with white tablecloths"></div>
      <div class="photo photo--dessert" role="img" aria-label="Chocolate lava cake with cream and mint"></div>
      <div class="photo photo--bar" role="img" aria-label="Restaurant bar and dining floor"></div>
    </div>

    <section class="events">
      <h2 class="events__heading">Great Choice For Your Next Private Event</h2>
      <p class="events__copy">We are proud to offer one private event space, as well as the opportunity for a full-facility event. Our restaurant is perfect for any occasion, whether it be a sit-down dinner or a standing cocktail reception</p>
    </section>

    <svg class="divider" viewBox="0 0 480 6" preserveAspectRatio="none" aria-hidden="true">
      <path d="M0,3 Q240,0 480,3 Q240,5 0,3 Z" fill="#2b2b2b"/>
    </svg>

    <section class="happy-hour">
      <h2 class="happy-hour__heading">Happy Hour is Served<br>Every Monday - Friday 3:00pm - 6:00pm</h2>
      <p class="happy-hour__menu">$5 Draft &nbsp;|&nbsp; $5 House Wine &nbsp;|&nbsp; $7 Select Cocktails<br>$1 Oysters &nbsp;|&nbsp; $5 Wood-Fired Pizzas</p>
    </section>

    <div class="photo-row photo-row--menu">
      <div class="photo photo--pizza" role="img" aria-label="Wood-fired pizza in front of the oven"></div>
      <div class="photo photo--oysters" role="img" aria-label="Platter of oysters on ice"></div>
      <div class="photo photo--cocktails" role="img" aria-label="Assorted cocktails on the bar"></div>
    </div>

    <div class="reserve-bar">FOR RESERVATION CALL &nbsp;925.555.0142</div>

    <div class="brand">Pelbar Kitchen</div>
    <div class="website">www.pelbarkitchen.com</div>
    <div class="social" aria-hidden="true">
      <span class="social__square"></span>
      <span class="social__square"></span>
    </div>
  </main>
</body>
</html>
```